Corvell Upholstery & Design
Stationary & Biz Card
Project: Corvell Upholstery & Design
Corvell Upholstery & Design -
Creative Brief
Bright & Fun-filled
Dorin Velasq
Owner
51847 Pellinore Court Ashbury, MD 21904
dorin@corvellupholstery-example.com
www.corvellupholstery-example.com

```html
<!DOCTYPE html>
<html lang="en">
<head>
<meta charset="utf-8">
<title>Corvell Interiors – Business Cards</title>
<link rel="stylesheet" href="https://fonts.googleapis.com/css2?family=Didact+Gothic&display=swap">
<style>
  :root {
    --bg: #e6e6e6;
    --card: #ffffff;
    --red: #e8262b;
    --red-dark: #c91d22;
    --grey: #7d7d7d;
    --ink: #3a3a3a;
    --rule: #bdbdbd;
    --on-red: rgba(255,255,255,0.6);
    --shadow: 0 6px 18px rgba(0,0,0,0.18);
  }
  * { box-sizing: border-box; margin: 0; padding: 0; }
  html, body {
    width: 1200px; height: 830px; overflow: hidden;
    background: var(--bg);
    font-family: "Didact Gothic", "Helvetica Neue", Arial, sans-serif;
  }
  .canvas { position: relative; width: 1200px; height: 830px; }
  .card {
    position: absolute; width: 540px; height: 300px;
    border-radius: 14px; overflow: hidden; box-shadow: var(--shadow);
  }
  .card--front { left: 330px; top: 50px; background: var(--card); }
  .card--red { left: 40px; top: 460px; background: var(--red); }
  .card--back { left: 620px; top: 460px; background: var(--card); }

  .brand { position: absolute; display: flex; align-items: center; gap: 12px; }
  .brand__dot {
    flex: none; width: 22px; height: 22px; border-radius: 50%;
    background: var(--red);
  }
  .brand__name { font-size: 26px; line-height: 1; color: var(--grey); white-space: nowrap; }

  .card--front .brand { left: 34px; top: 132px; }
  .card--front .brand__name { font-size: 24px; }
  .divider {
    position: absolute; left: 275px; top: 38px; width: 1px; height: 200px;
    background: var(--rule);
  }
  .contact { position: absolute; left: 292px; top: 40px; color: var(--ink); }
  .contact__name { color: var(--red); font-size: 17px; }
  .contact__role { font-size: 12px; margin-top: 3px; }
  .contact__details { font-size: 11.5px; line-height: 1.45; margin-top: 44px; }
  .contact__web { font-size: 11.5px; margin-top: 14px; }
  .card__band {
    position: absolute; left: 0; right: 0; bottom: 0; height: 10px;
    background: var(--red-dark);
  }

  .card--red .brand { left: 0; right: 0; bottom: 62px; justify-content: center; }
  .card--red .brand__name { color: var(--on-red); }

  .card--back .brand { right: 40px; bottom: 58px; }
</style>
</head>
<body>
<main class="canvas">
  <section class="card card--front" aria-label="Business card front">
    <div class="brand">
      <span class="brand__dot"></span>
      <span class="brand__name">Corvell Interiors</span>
    </div>
    <div class="divider"></div>
    <div class="contact">
      <p class="contact__name">Dorin Velasq</p>
      <p class="contact__role">Owner</p>
      <p class="contact__details">
        51847 Pellinore Court<br>
        Ashbury, MD 21904<br>
        P: 240-555-0141<br>
        C: 240-555-0142<br>
        F: 240-555-0143<br>
        E: dorin@corvellupholstery-example.com
      </p>
      <p class="contact__web">www.corvellupholstery-example.com</p>
    </div>
    <div class="card__band"></div>
  </section>

  <section class="card card--red" aria-label="Business card back, red">
    <div class="brand">
      <span class="brand__name">Corvell Interiors</span>
    </div>
  </section>

  <section class="card card--back" aria-label="Business card back, white">
    <div class="brand">
      <span class="brand__dot"></span>
      <span class="brand__name">Corvell Interiors</span>
    </div>
  </section>
</main>
</body>
</html>
```